Refresh of a rather different IT outfit website

Our web site is starting to show it's age. You can see the existing site here: www.plumbcorner.net. As a growing company we want to come across as a dynamic collection of IT experts.

We want to update the design so are open to any colour palette and look, but want to retain our current table logo. We use the logo on our business cards but with a white background - see the attached file, so you don't need to keep the brown or the green.

The design should consider the range of browsers that will be looking at the site - so please show how it will look on a wide screen laptop and a 768x1024 tablet.

We want to add some pages about our team and their skills, probably with photos of each person on the team.

This is an uncoded project - the PSD files of the design is required, not coding.
Updates

Thanks everyone for the submissions so far.  It's a holiday day in the UK today but we will get some feedback on the designs so far out to you.

Target Market(s)

Architects and other creative types looking for IT support

Industry/Entity Type

Business

Font styles to use
Serif
Sans Serif

Requirements
Must have
• Must look good on a laptop and an iPad.

```html
<!DOCTYPE html>
<html lang="en">
<head>
<meta charset="utf-8">
<title>plumbcorner — IT Support</title>
<link rel="stylesheet" href="https://fonts.googleapis.com/css2?family=Didact+Gothic&family=Dosis:wght@500;700&display=swap">
<style>
:root{
  --plum:#8f1a58;
  --plum-dark:#6e1243;
  --gold:#d8a80c;
  --hero:#4b4b4b;
  --page:#f4f4f4;
  --card:#f7f7f7;
  --ink:#555;
  --ink-soft:#777;
  --footer:#292929;
  --btn-grey:#666;
}
*{margin:0;padding:0;box-sizing:border-box}
html,body{width:744px;height:1200px;overflow:hidden}
body{position:relative;background:var(--page);font-family:"Didact Gothic",sans-serif;color:var(--ink)}
.abs{position:absolute}

.topbar{left:0;top:0;width:744px;height:18px;background:var(--plum);color:#fff;font-size:8.5px;letter-spacing:.3px}
.topbar .contact{position:absolute;right:54px;top:3px;display:flex;gap:10px;align-items:center}
.topbar .contact span{display:flex;align-items:center;gap:4px}
.social{display:flex;gap:4px}
.social i{display:block;width:11px;height:11px;border-radius:50%;background:#fff}
.topbar .social{position:absolute;right:8px;top:3px}

.header{left:0;top:18px;width:744px;height:84px;background:#f8f8f8}
.brand{left:50px;top:30px;display:flex;align-items:center;gap:8px;font-family:"Dosis",sans-serif;font-weight:700;font-size:27px;color:var(--plum);letter-spacing:.2px}
.brand b{display:block;width:20px;height:20px;background:var(--gold)}
.nav{top:38px;font-size:10.5px;color:#555;letter-spacing:.3px}

.hero{left:0;top:102px;width:744px;height:281px;background:var(--hero)}
.hero h1{left:58px;top:142px;font-family:"Dosis",sans-serif;font-weight:500;font-size:21px;line-height:20px;letter-spacing:2px;color:#fff}
.hero ul{left:62px;top:200px;width:220px;list-style:none;color:#eee;font-size:8.6px;line-height:14px;letter-spacing:.2px}
.hero li{position:relative;padding-left:17px;margin-bottom:7px}
.hero li svg{position:absolute;left:0;top:3px}
.btn{display:flex;align-items:center;justify-content:center;font-size:10px;letter-spacing:.4px;color:#fff}
.btn-plum{background:var(--plum);box-shadow:0 2px 0 var(--plum-dark)}
.btn-ghost{border:1px solid #ddd;color:#eee}
.monitor{left:362px;top:146px}

.card{top:420px;width:205px;height:256px;background:var(--card);border:1px solid #ddd;border-bottom:3px solid #ccc}
.card h2{height:22px;background:var(--plum);color:#fff;font-family:"Dosis",sans-serif;font-weight:500;font-size:11px;letter-spacing:1.2px;text-align:center;line-height:22px;margin:-1px -1px 0}
.card .photo{margin:9px 9px 0;height:103px;border:1px solid #ccc}
.card p{margin:13px 14px 0;text-align:center;font-size:9.2px;line-height:14px;color:#666;letter-spacing:.2px}
.card .btn{width:78px;height:22px;margin:10px auto 0;background:var(--btn-grey);font-size:8.5px;box-shadow:0 2px 0 #444}
.card .btn.active{background:var(--plum);box-shadow:0 2px 0 var(--plum-dark)}

.welcome{left:42px;top:726px;width:432px}
.welcome h2{font-family:"Dosis",sans-serif;font-weight:500;font-size:13.5px;letter-spacing:1px;color:var(--gold);padding-bottom:6px;border-bottom:1px solid #ccc}
.welcome h2 span{color:var(--plum)}
.welcome p{margin:14px 2px 0;font-size:10px;line-height:14px;color:#666;letter-spacing:.2px}

.testimonials{left:502px;top:728px;width:183px;height:198px;background:#f8f8f8;border:1px solid #e2e2e2;border-bottom:3px solid #d5d5d5}
.testimonials header{height:24px;background:var(--plum);color:#fff;font-family:"Dosis",sans-serif;font-weight:500;font-size:9.5px;letter-spacing:.6px;padding:6px 11px;margin:-1px -1px 0;display:flex;justify-content:space-between}
.dots{display:flex;gap:2px;align-items:center}
.dots i{width:6px;height:6px;border-radius:50%;background:#fff}
.dots i:first-child{background:var(--gold)}
.quote{display:flex;gap:9px;margin:0 9px;padding:10px 0 9px}
.quote+.quote{border-top:1px solid #ddd}
.quote .face{flex:none;width:35px;height:44px;border:1px solid #bbb;background:linear-gradient(#e9e9e9,#9a8a7f)}
.quote p{font-size:7.8px;line-height:10.2px;color:#777}
.quote cite{display:block;margin-top:5px;font-style:normal;color:#999}

.footer{left:0;top:974px;width:744px;height:196px;background:var(--footer);color:#fff}
.footer h3{position:absolute;top:36px;font-family:"Dosis",sans-serif;font-weight:500;font-size:11.5px;letter-spacing:1px}
.footer ul{position:absolute;top:67px;list-style:none;font-size:8.4px;line-height:18.5px;letter-spacing:.4px;color:#eee}
.field{position:absolute;background:#fff;color:#999;font-size:8px;padding:4px 6px;letter-spacing:.3px}
.send{position:absolute;left:578px;top:119px;width:100px;height:19px;background:var(--gold);box-shadow:0 2px 0 #a88100;font-size:8.5px}
.bottombar{left:0;top:1170px;width:744px;height:30px;background:var(--plum);color:#fff;font-size:8.4px;letter-spacing:.3px}
.bottombar .copy{position:absolute;left:63px;top:10px}
.bottombar .social{position:absolute;right:72px;top:7px;gap:7px}
.bottombar .social i{width:16px;height:16px}
</style>
</head>
<body>

<div class="abs topbar">
  <div class="contact">
    <span><svg width="9" height="6" viewBox="0 0 9 6"><rect width="9" height="6" fill="#fff"/><path d="M0 0l4.5 3.5L9 0" stroke="#8f1a58" stroke-width=".8" fill="none"/></svg>office@plumbcorner.net</span>
    <span><svg width="9" height="9" viewBox="0 0 9 9"><rect width="9" height="9" rx="1" fill="#fff"/><path d="M2.5 2c0 3 1.5 4.5 4.5 4.5l.3-1.3-1.3-.6-.6.7C4.5 4.9 4 4.4 3.7 3.5l.7-.6-.6-1.3z" fill="#8f1a58"/></svg><span style="font-size:10px">02-5550-0140</span></span>
  </div>
  <div class="social"><i></i><i></i><i></i></div>
</div>

<div class="abs header"></div>
<div class="abs brand"><b></b>plumbcorner</div>
<div class="abs nav" style="left:356px">Home</div>
<div class="abs nav" style="left:421px">About</div>
<div class="abs nav" style="left:486px">Services</div>
<div class="abs nav" style="left:564px">News Updates</div>
<div class="abs nav" style="left:670px">Contact</div>

<section class="abs hero"></section>
<div class="hero">
  <h1 class="abs">SERIOUS IT SUPPORT<br>FOR BUSINESS</h1>
  <ul class="abs">
    <li><svg width="11" height="9" viewBox="0 0 11 9"><path d="M1 4.5l3 3L10 1" stroke="#fff" stroke-width="2" fill="none"/></svg>Lorem ipsum dolor sit amet, consectetur adipi-scing elit. Phasellus tincidunt tellus leo.</li>
    <li><svg width="11" height="9" viewBox="0 0 11 9"><path d="M1 4.5l3 3L10 1" stroke="#fff" stroke-width="2" fill="none"/></svg>Lorem ipsum dolor sit amet, dipsu consectetur adipiscing elit.</li>
    <li><svg width="11" height="9" viewBox="0 0 11 9"><path d="M1 4.5l3 3L10 1" stroke="#fff" stroke-width="2" fill="none"/></svg>Ipsum dolor sit amet, dipsu consectetur adipi-scing elit.</li>
  </ul>
  <div class="abs btn btn-plum" style="left:63px;top:323px;width:77px;height:26px">Read more</div>
  <div class="abs btn btn-ghost" style="left:146px;top:323px;width:91px;height:26px">Contact us</div>
  <svg class="abs monitor" width="298" height="216" viewBox="0 0 298 216">
    <defs>
      <linearGradient id="screenFill" x1="0" y1="0" x2="1" y2="1">
        <stop offset="0" stop-color="#2e3a4a"/><stop offset=".5" stop-color="#7b8ea3"/><stop offset="1" stop-color="#303944"/>
      </linearGradient>
    </defs>
    <path d="M0 40 L40 0 H200 V216 H0 Z" fill="#3e3e3e"/>
    <rect x="30" y="0" width="268" height="186" rx="6" fill="#1b1b1b"/>
    <rect x="30" y="162" width="268" height="24" rx="3" fill="#dcdcdc"/>
    <path d="M135 186 H200 L210 216 H125 Z" fill="#bdbdbd"/>
    <rect x="38" y="12" width="246" height="140" fill="url(#screenFill)" role="img" aria-label="Hand touching a network of cloud and device icons"/>
  </svg>
</div>

<article class="abs card" style="left:36px">
  <h2>WHO WE ARE</h2>
  <div class="photo" role="img" aria-label="Business team reviewing papers at a desk" style="background:linear-gradient(135deg,#dfe8f2,#3c5d86 60%,#c7d4e3)"></div>
  <p>Lorem ipsum dolor sit amet, con-sectetur adipiscing elit. Nam dapibus blandit enim, eget pellentesque nibh ullamco arperdapibus blandit enim.</p>
  <div class="btn">Read more</div>
</article>
<article class="abs card" style="left:269px">
  <h2>WHAT WE DO</h2>
  <div class="photo" role="img" aria-label="Hand holding floating technology icons" style="background:linear-gradient(90deg,#5c5f63,#b9bcbf 50%,#2a2a2c)"></div>
  <p>Lorem ipsum dolor sit amet, con-sectetur adipiscing elit. Nam dapibus blandit enim, eget pellentesque nibh ullamco arperdapibus blandit enim.</p>
  <div class="btn active">Read more</div>
</article>
<article class="abs card" style="left:502px">
  <h2>NEWS UPDATES</h2>
  <div class="photo" role="img" aria-label="Newspaper with a coffee cup" style="background:linear-gradient(180deg,#555 0,#9a9a9a 25%,#e6e4df 45%,#f4f2ec)"></div>
  <p>Lorem ipsum dolor sit amet, con-sectetur adipiscing elit. Nam dapibus blandit enim, eget pellentesque nibh ullamco arperdapibus blandit enim.</p>
  <div class="btn">Read more</div>
</article>

<section class="abs welcome">
  <h2>WELCOME TO <span>PLUMBCORNER</span></h2>
  <p>Lorem ipsum dolor sit amet, consectetur adipiscing elit. Phasellus eget leo leo. Sed adipiscing mi orci, vel ultrices turpis mattis a. Quisque sed eros luctus, euismod ligula et, suscipit dolor. Sed suscipit tortor eget leo hendrerit semper. Sed et fermentum.</p>
  <p>Curabitur tristique vestibulum bibendum. Quisque eget varius eros. Nunc id laoreet sem. Nullam vulputate fringilla mi sit amet imperdiet. Lorem ipsum dtolor sit amet, consectetur adipiscing elit. Pellentesque habitant morbi tristique senectus et netus et malesuada fames ac turpis egestas.</p>
</section>

<aside class="abs testimonials">
  <header>Testimonials<span class="dots"><i></i><i></i><i></i></span></header>
  <div class="quote">
    <div class="face" role="img" aria-label="Portrait of a client"></div>
    <p>Lorem ipsum dolor sit amet, consect adipiscing elit. Pha-sellus eget leo. Sed lipsum dolor mi orci<cite>- Adam Reyes, Talent</cite></p>
  </div>
  <div class="quote">
    <div class="face" role="img" aria-label="Portrait of a client"></div>
    <p>Lorem ipsum dolor sit amet, consect adipiscing elit. Pha-sellus eget leo. Sed lipsum dolor mi orci<cite>- Owen Blake, Manager</cite></p>
  </div>
</aside>

<footer class="abs footer">
  <h3 style="left:62px">ABOUT US</h3>
  <h3 style="left:172px">SERVICES OFFERED</h3>
  <h3 style="left:326px">ADDITIONAL INFO</h3>
  <h3 style="left:471px">QUICK MESSAGE</h3>
  <ul style="left:64px"><li>Who we are</li><li>Client List</li><li>Partners</li><li>Contact Info</li></ul>
  <ul style="left:175px"><li>Link goes here</li><li>Link goes here</li><li>Link goes here</li><li>Link goes here</li></ul>
  <ul style="left:328px"><li>Sitemap</li><li>FAQ</li><li>Privacy Policy</li><li>Terms &amp; Agreement</li></ul>
  <div class="field" style="left:472px;top:67px;width:100px;height:19px">Firstname</div>
  <div class="field" style="left:472px;top:92px;width:100px;height:19px">Email Address</div>
  <div class="field" style="left:472px;top:119px;width:100px;height:19px">Contact #</div>
  <div class="field" style="left:578px;top:67px;width:100px;height:44px">Message</div>
  <div class="btn send">Send Message</div>
</footer>

<div class="abs bottombar">
  <span class="copy">PlumbCorner.netAll Rights Reserved ® 2014</span>
  <div class="social"><i></i><i></i><i></i></div>
</div>

</body>
</html>
```